Infoblatt
Zielgruppe
Talentförderung, Personalentwicklung, Beratung von Personalabteilungen
Zielgruppe: Personaler, HR Verantwortliche
Aufgabenstellung
Es geht um einen "One-Pager", der auf einem Kongress ausgelegt werden soll und in Kurzform einen Überblick über unser Unternehmen und unser Angebot informieren soll.
Wir haben Visitenkarten auf Recyclingpapier und möchten das Blatt konsistent auf das gleiche Papier drucken lassen, daher einfarbig schwarz. Format DIN A4 Hoch.
IDEE: Vom Stil wie eine Infografik aufbauen
TYPO: unser LOGO ist BEBAS NEUE und unsere Schrift Helvetica

```html
<!DOCTYPE html>
<html lang="de">
<head>
<meta charset="utf-8">
<title>Infoblatt</title>
<link href="https://fonts.googleapis.com/css2?family=Cedarville+Cursive&family=Source+Sans+3:wght@400;600;700&display=swap" rel="stylesheet">
<style>
  :root {
    --backdrop: #efefef;
    --paper: #ffffff;
    --ink: #2b2b2b;
    --ink-soft: #3a3a3a;
    --panel-dark: #333333;
    --on-dark: #f2f2f2;
    --photo-light-a: #e6e6e6;
    --photo-light-b: #c9c9c9;
    --photo-mid-a: #8a8a8a;
    --photo-mid-b: #3c3c3c;
  }
  * { box-sizing: border-box; margin: 0; padding: 0; }
  html, body { width: 1200px; height: 850px; overflow: hidden; }
  body {
    background: radial-gradient(ellipse at center, #fafafa 0%, var(--backdrop) 70%, #e4e4e4 100%);
    font-family: "Source Sans 3", "Helvetica Neue", Arial, sans-serif;
    position: relative;
  }
  .sheet {
    position: absolute;
    left: 330px; top: 45px;
    width: 536px; height: 757px;
    background: var(--paper);
    display: grid;
    grid-template-columns: 268px 268px;
    grid-template-rows: 205px 280px 272px;
    overflow: hidden;
  }
  .cell { position: relative; overflow: hidden; }
  .photo { position: absolute; inset: 0; }
  .photo--wood-light { background: linear-gradient(90deg, #efefef 0%, #e2e2e2 45%, #d0d0d0 70%, #bdbdbd 100%); }
  .photo--dartboard { background: radial-gradient(circle at 58% 70%, #9a9a9a 0%, #5a5a5a 35%, #3a3a3a 60%, #7a7a7a 100%); }
  .photo--meeting { background: linear-gradient(110deg, #cfcfcf 0%, #9a9a9a 30%, #3a3a3a 60%, #d8d8d8 100%); }
  .photo--desk-light { background: linear-gradient(180deg, #d6d6d6 0%, #e6e6e6 45%, #f1f1f1 100%); }
  .photo--flipchart { background: linear-gradient(180deg, #555 0%, #6e6e6e 35%, #a8a8a8 60%, #d8d8d8 100%); }
  .panel-dark { background: var(--panel-dark); color: var(--on-dark); }
  .content { position: relative; padding: 0 24px; }
  .headline {
    font-family: "Cedarville Cursive", cursive;
    font-weight: 400;
    font-size: 27px;
    line-height: 1;
    letter-spacing: 0.5px;
  }
  .copy { font-size: 9.2px; line-height: 13.6px; color: var(--ink-soft); }
  .panel-dark .copy { color: var(--on-dark); }
  .copy p + p { margin-top: 6px; }
  .copy strong { font-weight: 700; color: var(--ink); }
  .group-title { font-weight: 700; font-size: 9px; letter-spacing: 0.3px; margin-top: 10px; }
  .bullets { list-style: none; }
  .bullets li::before { content: "•"; margin-right: 5px; }
  .belief .content { padding-top: 47px; color: var(--ink); }
  .belief .headline { margin-bottom: 15px; }
  .offer .content { padding-top: 40px; }
  .offer .headline { margin-bottom: 16px; color: #fff; }
  .principles .content { padding-top: 30px; color: var(--ink); }
  .principles .headline { line-height: 0.9; margin-bottom: 18px; }
</style>
</head>
<body>
  <main class="sheet">
    <section class="cell belief">
      <div class="photo photo--wood-light" role="img" aria-label="Helles Schwarzweißfoto einer Holzwand"></div>
      <div class="content">
        <h2 class="headline">Woran wir glauben</h2>
        <div class="copy">
          <p>Wir glauben, dass sich persönliche und ökonomische Werte ergänzen - mehr noch, dass sie langfristig nicht ohne einander auskommen und dass sich emotionale Bindung als Mehrwert in Zahlen ausdrückt.</p>
        </div>
      </div>
    </section>

    <div class="cell">
      <div class="photo photo--dartboard" role="img" aria-label="Schwarzweißfoto einer Dartscheibe"></div>
    </div>

    <div class="cell">
      <div class="photo photo--meeting" role="img" aria-label="Unscharfes Schwarzweißfoto einer Besprechung im Büro"></div>
    </div>

    <section class="cell panel-dark offer">
      <div class="content">
        <h2 class="headline">Was wir bieten</h2>
        <div class="copy">
          <p>Wir beraten Unternehmen im Rahmen der Talentförderung und helfen Jugendlichen auf dem Weg in ihr Berufsleben.</p>
          <h3 class="group-title">FÜR UNTERNEHMEN</h3>
          <ul class="bullets">
            <li>Talentförderung &amp; Talent Management</li>
            <li>Professionalisierung der Personalarbeit</li>
            <li>Organisationsentwicklung</li>
            <li>Potentialorientierte Mitarbeiterführung</li>
          </ul>
          <h3 class="group-title">FÜR DIE JUNGE GENERATION</h3>
          <ul class="bullets">
            <li>Berufsorientierung</li>
            <li>Bewerbungscoaching</li>
          </ul>
        </div>
      </div>
    </section>

    <section class="cell principles">
      <div class="photo photo--desk-light" role="img" aria-label="Helles Schwarzweißfoto eines Schreibtischs mit Papierrolle"></div>
      <div class="content">
        <h2 class="headline">Was unser<br>Handeln leitet</h2>
        <div class="copy">
          <p>Kundare heißt marktschreierisch anpreisen, hinters Licht führen, täuschen. Mandare heißt beauftragen, Vertrauen schenken. Wir legen großen Wert auf eine Beziehung, die Mandare, nicht Kundare entspricht.</p>
          <p>Für uns ist der partnerschaftliche Umgang mit unseren Mandanten das Fundament.</p>
          <p><strong>Wir haben keine Kunden.<br>Wir unterstützen Mandanten.</strong></p>
        </div>
      </div>
    </section>

    <div class="cell">
      <div class="photo photo--flipchart" role="img" aria-label="Schwarzweißfoto eines Flipcharts mit Notizen und Markern"></div>
    </div>
  </main>
</body>
</html>
```